依頼詳細
人工知能(AI)というデジタルでクールなイメージと、教育というアナログで優しいイメージを合わせもった雰囲気のWebサイトを構築したいと考えています。
海外のデザイナーにたたき台となるデザインをしていただいたのですが、やはり日本のデザインとは異なるところが多くあり、日本のデザイナーさんに再度依頼しようと決めました。
他の案件と比べるとたたき台となるWebデザインや営業用のフライヤーまでそろっていますので、色やデザインの印象がつかみやすいと思います。

現ホームページもありますが、会社の内容であったりをつかみにくいため、もっとわかりやすく華やかな印象があり信頼できるページのデザインに仕上げたいと考えています。

こちらに「たたき台となる海外のデザイナーによるWebデザイン」と「日本のデザイナーによるフライヤー(完成版)」の画像がありますので、大きく参考になると思いますので、必ずすべての画像を見ていただいてから作業の開始をお願いします。
https://files.norebun.jp/share/folders/83kqpwZTRmvbhaa41xLoyy0cMEFdPZn7?usp=sharing

海外のデザイナーさんは悪くはないのですが、やはり日本のデザインとは異なり、もう少し日本らしいデザインで信頼性を確保したいと思っています。

今回はこの「トップページ」に関して作成をお願いします。
言葉に関しては後から埋めていけますので、ダミーで入れていただければと思います。

私の好きなサイトデザインを挙げておきますので、ご参考まで。
https://www.tovrex.jp/
https://mizu-lab.in/

単なるまねではなく、個性がしっかりと出ていて、求めていたデザインとなる方と一緒に理想のデザインを求めていければ幸いです。

みなさま、どうぞよろしくお願いいたします。
サイトURL
https://www.sorumina.co.jp/
ページ数
1ページ
希望イメージ
シンプル 複雑
単色 カラフル
暗い 明るい
日常 高級
遊び心 厳粛
未来的 伝統的
女性的 男性的
希望する色
青系、水色系
納品ファイル
• 高解像度JPG (.jpg)
• イラストレーター形式 (.ai)
• フォトショップ形式 (.psd)
補足説明
画像ファイルなどは詳細依頼をご確認ください。
■ 選んだ理由

依頼内容に記載した内容だけではなく、弊社のHPやインタビュー記事なども参考にしていただき、会社の方針を汲み取り、デザインに上手く反映していただいた点から選ばさせていただきました。

■ 提案者全員のお礼・コメント

この度は、既にあるデザインの再構成という一般的な依頼内容とは少し毛色が違うご依頼になってしまったにも関わらず、多数のご提案をありがとうございました。
また、ご縁がございましたら、何卒、よろしくお願いいたします。

```html
<!DOCTYPE html>
<html lang="ja">
<head>
<meta charset="UTF-8">
<title>ソルミナ | ビジネス目線で機械学習を教育する</title>
<link href="https://fonts.googleapis.com/css2?family=Noto+Sans+JP:wght@400;500;700&family=Montserrat:wght@600;700&display=swap" rel="stylesheet">
<style>
:root{
  --blue:#1587d6;
  --blue-deep:#0a64b4;
  --sky:#e8f4fc;
  --navy:#1d2b3a;
  --ink:#333b44;
  --muted:#7a8591;
  --line:#dbe3ea;
  --teal:#0f8f9a;
  --white:#ffffff;
}
*{margin:0;padding:0;box-sizing:border-box}
html,body{width:1200px;height:4608px;overflow:hidden}
body{font-family:"Noto Sans JP",sans-serif;color:var(--ink);background:var(--white);position:relative;font-size:14px;line-height:1.8}
section,header,footer{position:absolute;left:0;width:1200px}
.abs{position:absolute}
.btn{position:absolute;display:flex;align-items:center;justify-content:center;background:var(--blue);color:var(--white);font-size:14px;font-weight:500;height:46px;border-radius:2px}
.btn::after{content:"›";margin-left:12px;font-size:18px}
.section-title{position:absolute;left:0;width:1200px;text-align:center;color:var(--blue);font-size:30px;font-weight:700;letter-spacing:.08em}
.section-title::after{content:"";display:block;width:40px;height:3px;background:var(--blue);margin:14px auto 0}
.ph{position:absolute}
.dummy{font-size:13px;color:var(--ink);line-height:1.9}

/* header */
.site-header{top:0;height:56px;background:var(--white);box-shadow:0 1px 4px rgba(0,0,0,.08);z-index:5}
.brand{position:absolute;left:40px;top:12px;display:flex;align-items:center;gap:10px}
.brand-dot{width:30px;height:30px;border-radius:50%;background:var(--blue)}
.brand-name{font-size:18px;font-weight:700;color:var(--navy);line-height:1}
.brand-sub{font-size:8px;font-weight:700;color:var(--navy);letter-spacing:.2em;line-height:1.2}
.global-nav{position:absolute;right:40px;top:0;height:56px;display:flex;align-items:center;gap:30px;font-size:13px;color:var(--navy)}
.global-nav .contact{background:var(--white);border:1px solid var(--blue);color:var(--blue);padding:6px 16px;font-weight:500}

/* hero */
.hero{top:56px;height:460px;background:linear-gradient(160deg,#cdd6de 0%,#9aa8b5 45%,#5b6d80 100%)}
.hero-word{position:absolute;top:170px;width:200px;height:70px;border:1px solid rgba(255,255,255,.8);background:rgba(255,255,255,.18);color:var(--white);font-size:30px;font-weight:500;display:flex;align-items:center;justify-content:center;letter-spacing:.1em}
.hero-x{position:absolute;top:175px;left:585px;color:var(--white);font-size:40px}
.lead-card{top:440px;left:240px;width:720px;height:150px;background:var(--white);box-shadow:0 6px 20px rgba(0,0,0,.12);text-align:center;padding-top:36px;z-index:3}
.lead-card h1{font-size:28px;color:var(--blue-deep);font-weight:700;letter-spacing:.06em}
.lead-card p{font-size:14px;color:var(--ink);margin-top:8px}

/* why */
.why{top:590px;height:370px;background:var(--white)}
.why h2{position:absolute;left:600px;top:90px;font-size:18px;color:var(--blue-deep);font-weight:700}
.why .dummy{position:absolute;left:600px;width:430px}

/* can-do */
.can-do{top:960px;height:1080px;background:linear-gradient(180deg,var(--sky) 0%,#f5fafe 60%,var(--sky) 100%)}
.can-do .intro{position:absolute;top:130px;left:0;width:1200px;text-align:center;font-size:14px;line-height:1.9}
.target-card{position:absolute;top:220px;width:390px;height:140px;background:var(--white);box-shadow:0 2px 8px rgba(0,0,0,.06);display:flex;gap:16px;padding:20px}
.target-card .thumb{width:110px;height:100px;flex:none}
.target-card h3{font-size:14px;color:var(--blue);font-weight:700}
.target-card p{font-size:12px;line-height:1.8}
.cycle-lead{position:absolute;top:400px;left:0;width:1200px;text-align:center;font-size:18px;font-weight:500;color:var(--navy);line-height:1.8}
.cycle-label{position:absolute;width:210px;font-size:12px}
.cycle-label strong{display:block;font-family:"Montserrat",sans-serif;font-size:20px;font-weight:700;line-height:1.2}
.cycle-label span{font-weight:700;font-size:14px}

/* strengths */
.strengths{top:2040px;height:260px;background:var(--blue-deep)}
.strength-card{position:absolute;top:40px;width:300px;height:180px;background:var(--white);padding:18px 20px;text-align:center}
.strength-card h3{font-size:15px;color:var(--blue-deep);font-weight:700}
.strength-card p{font-size:11px;line-height:1.7;margin-top:6px;color:var(--ink)}
.partner-row{display:flex;justify-content:center;gap:14px;margin-top:14px}
.partner-mark{width:70px;height:26px;background:#d7dde3}

/* services */
.services{top:2300px;height:660px;background:var(--white)}
.service-item{position:absolute;top:170px;width:460px}
.service-item h3{font-size:17px;color:var(--blue-deep);font-weight:700;margin-top:22px}
.service-item p{font-size:12px;line-height:1.8;margin-top:6px}

/* events */
.events{top:2960px;height:310px;background:linear-gradient(180deg,#3c4650,#252c33)}
.events h2{position:absolute;top:24px;width:1200px;text-align:center;color:var(--white);font-size:20px;font-weight:700;letter-spacing:.08em}
.event-card{position:absolute;top:76px;width:225px}
.event-card .thumb{height:120px}
.event-card h3{font-size:13px;color:var(--white);margin-top:10px;font-weight:700}
.event-card p{font-size:11px;color:#c9d1d9;line-height:1.6}
.arrow{position:absolute;top:120px;width:40px;height:40px}

/* news */
.news{top:3270px;height:410px;background:var(--white)}
.news-col{position:absolute;top:50px;width:430px}
.news-col h2{font-size:18px;color:var(--blue-deep);font-weight:700;padding-bottom:10px;border-bottom:2px solid var(--blue)}
.news-item{padding:12px 0;border-bottom:1px solid var(--line)}
.news-item time{display:block;color:var(--blue);font-size:13px;font-family:"Montserrat",sans-serif;font-weight:600}
.news-item p{font-size:12px;line-height:1.7}

/* gateway */
.gateway{top:3680px;height:440px}
.gate{position:absolute;top:0;width:600px;height:440px;display:flex;flex-direction:column;align-items:center;justify-content:center;gap:26px}
.gate h2{color:var(--white);font-size:26px;font-weight:700;letter-spacing:.1em}
.gate .link{background:var(--navy);color:var(--white);width:200px;height:44px;display:flex;align-items:center;justify-content:center;font-size:14px}

/* footer */
.site-footer{top:4120px;height:460px;background:var(--white)}
.footer-address{position:absolute;left:130px;top:150px;font-size:13px;line-height:1.9}
.footer-links{position:absolute;top:70px;list-style:none;font-size:13px;line-height:2.3}
.footer-links li::before{content:"";display:inline-block;width:6px;height:6px;background:var(--blue);border-radius:50%;margin-right:10px;vertical-align:middle}
.footer-links .head{font-weight:700;color:var(--navy)}
.footer-links .head::before{display:none}
.copyright{top:4580px;height:28px;background:var(--blue-deep);color:var(--white);font-size:11px;display:flex;align-items:center;justify-content:center}
</style>
</head>
<body>

<header class="site-header">
  <div class="brand">
    <div class="brand-dot"></div>
    <div><div class="brand-name">ソルミナ</div><div class="brand-sub">SORUMINA</div></div>
  </div>
  <nav class="global-nav">
    <span>機械学習とは</span><span>私たちについて</span><span>サービス一覧</span><span>採用情報</span><span class="contact">お問い合わせ</span>
  </nav>
</header>

<section class="hero">
  <div class="ph" role="img" aria-label="ビジネスパーソンが机を囲んで話し合う写真" style="inset:0;background:linear-gradient(160deg,#d6dde4 0%,#a3b0bc 45%,#4f6176 100%)"></div>
  <div class="hero-word" style="left:330px">機械学習</div>
  <div class="hero-x">×</div>
  <div class="hero-word" style="left:670px">ビジネス</div>
</section>

<div class="lead-card abs">
  <h1>「ビジネス目線で機械学習を教育する」</h1>
  <p>「ビジネスの現場」で機械学習を活用できる人材・組織を育てます</p>
</div>

<section class="why">
  <div class="ph" role="img" aria-label="タブレットを手に微笑む女性の写真" style="left:180px;top:80px;width:360px;height:260px;background:linear-gradient(135deg,#f1f4f7,#cfd8e0)"></div>
  <h2>なぜ機械学習が必要なのか？</h2>
  <p class="dummy" style="top:130px">業務の多くはデータで動いています。機械学習を理解することで、日々の判断を速く正確にし、新しい価値を生み出す力が組織に備わります。現場の課題から考える姿勢が大切です。</p>
  <p class="dummy" style="top:230px">私たちは技術だけでなく、ビジネスの視点から活用方法を丁寧にお伝えし、学んだ知識を実務へつなげるお手伝いをします。</p>
  <div class="btn" style="left:880px;top:300px;width:150px;height:38px;font-size:13px">詳しく見る</div>
</section>

<section class="can-do">
  <h2 class="section-title" style="top:50px">ソルミナができること</h2>
  <p class="intro">個人のスキルからチームを育てることで、ビジネスの成果に結びつく力を伸ばすカリキュラム<br>「経営層」「エンジニア層」双方をターゲットとした機械学習に関するコンサル・教育事業を行っています。</p>
  <div class="target-card" style="left:200px">
    <div class="thumb" role="img" aria-label="講義を受けるエンジニアのイメージ" style="background:linear-gradient(135deg,#e4ecf3,#b9c8d6)"></div>
    <div><h3>エンジニア向け</h3><p>機械学習を理解し、サービスを作り上げるための実践的な講座と演習を用意しています。</p></div>
  </div>
  <div class="target-card" style="left:610px">
    <div class="thumb" role="img" aria-label="打ち合わせをする経営層のイメージ" style="background:linear-gradient(135deg,#e4ecf3,#b9c8d6)"></div>
    <div><h3>経営層向け</h3><p>機械学習の価値を理解し、投資判断と組織づくりに役立つ研修を行います。</p></div>
  </div>
  <p class="cycle-lead">現場での機械学習を加速させるには、<br>経営者層とエンジニアが共通理解を持つことが不可欠です。</p>

  <svg class="abs" style="left:0;top:500px" width="1200" height="380" viewBox="0 0 1200 380" aria-hidden="true">
    <g fill="none" stroke-width="34">
      <path d="M490 190 A110 110 0 0 1 600 80" stroke="#7cc242"/>
      <path d="M600 80 A110 110 0 0 1 710 190" stroke="#1587d6"/>
      <path d="M710 190 A110 110 0 0 1 600 300" stroke="#f5a623"/>
      <path d="M600 300 A110 110 0 0 1 490 190" stroke="#e2574c"/>
    </g>
    <g fill="#7a8591" font-size="11" font-family="Noto Sans JP,sans-serif"></g>
    <g stroke="#b7c3ce" stroke-width="1">
      <line x1="470" y1="80" x2="330" y2="80"/><line x1="730" y1="80" x2="870" y2="80"/>
      <line x1="730" y1="300" x2="870" y2="300"/><line x1="470" y1="300" x2="330" y2="300"/>
    </g>
    <circle cx="490" cy="80" r="16" fill="#7cc242"/><circle cx="710" cy="80" r="16" fill="#1587d6"/>
    <circle cx="710" cy="300" r="16" fill="#f5a623"/><circle cx="490" cy="300" r="16" fill="#e2574c"/>
  </svg>
  <div class="cycle-label" style="left:320px;top:530px;color:#7cc242"><strong>PLAN</strong><span>計画</span></div>
  <div class="cycle-label" style="left:760px;top:530px;color:var(--blue)"><strong>DO</strong><span>実行・モデル構築</span></div>
  <div class="cycle-label" style="left:760px;top:750px;color:#f5a623"><strong>CHECK</strong><span>評価・モデル検証</span></div>
  <div class="cycle-label" style="left:320px;top:750px;color:#e2574c"><strong>ACTION</strong><span>改善・再設計</span></div>
  <div class="btn" style="left:480px;top:960px;width:240px">サービスについて詳しく見る</div>
</section>

<section class="strengths">
  <div class="strength-card" style="left:130px">
    <h3>大手AI企業と協業</h3>
    <p>業界大手の企業と協力し、機械学習を学ぶための教材と研修プログラムを提供しています。</p>
    <div class="partner-row"><div class="partner-mark"></div><div class="partner-mark"></div></div>
  </div>
  <div class="strength-card" style="left:450px">
    <h3>公的機関認定講座</h3>
    <p>「第四次産業革命スキル習得講座」の認定を受けた講座で、給付金の対象となります。</p>
    <div class="partner-row"><div class="partner-mark"></div><div class="partner-mark" style="width:40px"></div></div>
  </div>
  <div class="strength-card" style="left:770px">
    <h3>共同プロジェクト多数</h3>
    <p>データサイエンス人材を育成する共同プロジェクトを多数進めています。</p>
    <div class="partner-row"><div class="partner-mark"></div><div class="partner-mark"></div></div>
  </div>
</section>

<section class="services">
  <h2 class="section-title" style="top:50px">ソルミナのサービス</h2>
  <div class="service-item" style="left:130px">
    <div class="ph" role="img" aria-label="セミナーで講義を聞く受講者の写真" style="position:relative;height:260px;background:linear-gradient(135deg,#c9d3dc,#6f8194)"></div>
    <h3>セミナー（短期／長期）</h3>
    <p>短期集中型から長期の育成講座まで、目的に合わせた受講形態をご用意しています。お気軽にご相談ください。</p>
    <div class="btn" style="left:0;top:390px;width:300px">セミナー事業について詳しく見る</div>
  </div>
  <div class="service-item" style="left:610px">
    <div class="ph" role="img" aria-label="企業研修で説明を受ける社員の写真" style="position:relative;height:260px;background:linear-gradient(135deg,#d2dbe3,#7b8ea1)"></div>
    <h3>企業内人材育成支援</h3>
    <p>貴社の課題に合わせた研修を設計し、社内で機械学習を推進できる人材を育てます。</p>
    <div class="btn" style="left:0;top:390px;width:300px">企業内人材育成について詳しく見る</div>
  </div>
</section>

<section class="events">
  <h2>イベント・ハンズオンセミナー</h2>
  <svg class="arrow" style="left:50px" viewBox="0 0 40 40" aria-hidden="true"><path d="M25 8 L13 20 L25 32" fill="none" stroke="#fff" stroke-width="3"/></svg>
  <svg class="arrow" style="right:50px" viewBox="0 0 40 40" aria-hidden="true"><path d="M15 8 L27 20 L15 32" fill="none" stroke="#fff" stroke-width="3"/></svg>
  <div class="event-card" style="left:110px"><div class="thumb" role="img" aria-label="セミナー会場の写真" style="background:linear-gradient(135deg,#b8c4cf,#6d7d8c)"></div><h3>セミナータイトル</h3><p>開催日時と内容の概要が入ります。</p></div>
  <div class="event-card" style="left:365px"><div class="thumb" role="img" aria-label="ハンズオン講座の告知画像" style="background:linear-gradient(135deg,#e3edf5,#9bb8cf)"></div><h3>セミナータイトル</h3><p>開催日時と内容の概要が入ります。</p></div>
  <div class="event-card" style="left:620px"><div class="thumb" role="img" aria-label="講師が登壇する写真" style="background:linear-gradient(135deg,#c5d0da,#74879a)"></div><h3>セミナータイトル</h3><p>開催日時と内容の概要が入ります。</p></div>
  <div class="event-card" style="left:875px"><div class="thumb" role="img" aria-label="受講者が演習に取り組む写真" style="background:linear-gradient(135deg,#bfcad4,#6a7b8b)"></div><h3>セミナータイトル</h3><p>開催日時と内容の概要が入ります。</p></div>
</section>

<section class="news">
  <div class="news-col" style="left:130px">
    <h2>新着情報</h2>
    <div class="news-item"><time>2018/04/09</time><p>新しい講座の募集を開始しました。詳細はお知らせページをご覧ください。</p></div>
    <div class="news-item"><time>2018/04/09</time><p>春期セミナーの日程を公開しました。お早めにお申し込みください。</p></div>
    <div class="news-item"><time>2018/04/09</time><p>年末年始の営業日についてのお知らせを掲載しました。</p></div>
  </div>
  <div class="news-col" style="left:640px">
    <h2>ブログ</h2>
    <div class="news-item"><time>2018/04/09</time><p>機械学習を業務に導入するときに最初に考えるべきこと。</p></div>
    <div class="news-item"><time>2018/04/09</time><p>講座の受講者に聞いた、学びを現場で活かすためのコツ。</p></div>
    <div class="news-item"><time>2018/04/09</time><p>データ分析の基礎をやさしく解説するシリーズ第三回。</p></div>
  </div>
</section>

<section class="gateway">
  <div class="gate" role="img" aria-label="明るいオフィス内の写真" style="left:0;background:linear-gradient(135deg,rgba(15,143,154,.85),rgba(10,100,120,.9)),#5a7a80">
    <h2>会社概要</h2><div class="link">詳しく見る ›</div>
  </div>
  <div class="gate" role="img" aria-label="笑顔で並ぶ社員の写真" style="left:600px;background:linear-gradient(135deg,rgba(21,135,214,.8),rgba(10,80,160,.9)),#5f7590">
    <h2>採用情報</h2><div class="link">詳しく見る ›</div>
  </div>
</section>

<footer class="site-footer">
  <div class="brand" style="left:130px;top:80px">
    <div class="brand-dot"></div>
    <div><div class="brand-name">ソルミナ</div><div class="brand-sub">SORUMINA</div></div>
  </div>
  <p class="footer-address">〒150-0042<br>東京都渋谷区宇田川町5丁目3-8 宇田川ビル2階 201号室</p>
  <ul class="footer-links" style="left:640px">
    <li>ホーム</li><li>機械学習とは</li><li>私たちについて</li><li>会社概要</li><li>採用情報</li><li>新着情報</li><li>ブログ</li>
  </ul>
  <ul class="footer-links" style="left:860px">
    <li class="head">サービス</li><li>短期セミナー</li><li>長期セミナー</li><li>企業内人材育成支援</li><li>お問い合わせ</li>
  </ul>
</footer>
<div class="copyright abs" style="left:0;width:1200px">Copyright © 株式会社ソルミナ All Rights Reserved.</div>

</body>
</html>
```